Waterjet Cutting Business requires an up to date website

We currently have a website which is outdated and in need of modernization.
We are only looking for a simple website with around 4 pages: Home, Contact Us, Materials, Gallery.
We have some pictures and a logo which can be used.
Our primary business is profile cutting of materials to customers specifications using high-pressure water with abrasive.
We are looking for creative ideas and are open to suggestions!
http://brimfieldcutworks.com/index.asp?pid=1
Update:
Cut quality picture (uploaded)
Map
Comparison to other profile cutting methods such as plasma/laser
Single page style without continuous scrolling
"We can cut virtually any material from any drawing whether it be a Full 3D cad models to hand sketched "
Target Market(s)
Film Industry, Prototype, Engineering, Architect, Artisits, one off designs
Industry/Entity Type
Engineering
Number of Pages Required
1 page
Font styles to use
Look and feel

```html
<!DOCTYPE html>
<html lang="en">
<head>
<meta charset="utf-8">
<title>Brimfield Cutworks</title>
<link href="https://fonts.googleapis.com/css2?family=Alegreya+Sans:wght@300;400;500&family=Open+Sans:wght@400;600;700&family=Arimo:wght@400;700&display=swap" rel="stylesheet">
<style>
:root{
  --blue:#2f74b8;
  --blue-dark:#23598f;
  --ink:#333333;
  --grey:#555555;
  --muted:#6b6b6b;
  --light:#ececec;
  --white:#ffffff;
  --night:#1f232a;
  --footer:#26282b;
}
*{margin:0;padding:0;box-sizing:border-box}
html,body{width:1200px;height:2875px;overflow:hidden}
body{position:relative;background:var(--white);font-family:"Arimo",Arial,sans-serif;color:var(--ink)}
.abs{position:absolute}
.heading{font-family:"Alegreya Sans",sans-serif;font-weight:400}

/* header */
.site-header{position:absolute;left:0;top:0;width:1200px;height:90px;background:var(--white)}
.brand{position:absolute;left:77px;top:22px;display:flex;align-items:center;gap:14px}
.brand-mark{width:34px;height:34px;background:var(--blue)}
.brand-name{font-family:"Open Sans",sans-serif;font-weight:700;font-size:28px;color:var(--blue);letter-spacing:1px}
.contact-item{position:absolute;top:25px;display:flex;gap:14px;align-items:flex-start}
.contact-icon{width:36px;height:36px;background:var(--blue);border-radius:3px;display:flex;align-items:center;justify-content:center}
.contact-label{font-size:14px;color:var(--muted);line-height:18px}
.contact-value{font-size:15px;color:var(--ink);line-height:20px}
.social-top{position:absolute;left:1040px;top:36px;display:flex;gap:16px}
.social-top span{width:13px;height:13px;border-radius:50%;background:#9a9a9a}

/* nav */
.main-nav{position:absolute;left:77px;top:90px;width:1044px;height:61px}
.main-nav .nav-band{position:absolute;left:0;top:0}
.main-nav ul{position:absolute;inset:0;list-style:none}
.main-nav li{position:absolute;top:20px;font-size:16px;color:var(--white)}

/* hero */
.hero{position:absolute;left:0;top:90px;width:1200px;height:583px;background:var(--light);overflow:hidden}
.hero .hero-art{position:absolute;left:0;top:0}
.hero-title{position:absolute;right:79px;top:135px;text-align:right;font-family:"Open Sans",sans-serif;font-weight:600;line-height:66px}
.hero-title .l1{font-size:60px;color:var(--blue);letter-spacing:2px}
.hero-title .l2{font-size:56px;color:#4a4a4a;letter-spacing:2px}
.hero-text{position:absolute;right:79px;top:282px;width:325px;text-align:right;font-size:14.5px;line-height:26px;color:var(--blue)}
.btn{position:absolute;background:var(--blue);color:var(--white);font-family:"Alegreya Sans",sans-serif;font-size:18px;border-radius:4px;display:flex;align-items:center;justify-content:center}
.hero .hero-arrows{position:absolute;left:1008px;top:508px}

/* welcome */
.welcome-kicker{left:80px;top:738px;font-size:40px;font-weight:300;color:#4a4a4a}
.welcome-title{left:80px;top:787px;font-size:42px;color:var(--blue);letter-spacing:1px}
.lead{font-size:19px;line-height:30px;color:var(--blue)}
.body-text{font-size:14.5px;line-height:26px;color:var(--grey)}
.frame{position:absolute;border:4px solid var(--blue)}
.photo{position:absolute}

/* gallery */
.gallery{position:absolute;left:0;top:1208px;width:1200px;height:625px;background:linear-gradient(160deg,#3a414c 0%,#1c2027 55%,#2a3038 100%)}
.gallery-title{position:absolute;left:0;width:1200px;top:62px;text-align:center;font-size:40px;color:var(--white)}
.tile{position:absolute}

/* newsletter */
.newsletter{position:absolute;left:0;top:2364px;width:1200px;height:157px;background:var(--light)}
.newsletter-band{position:absolute;left:0;top:0;width:520px;height:157px;background:var(--blue)}
.newsletter h3{position:absolute;left:132px;top:36px;font-size:30px;color:var(--white)}
.newsletter p{position:absolute;left:132px;top:82px;font-size:18px;color:var(--white)}
.newsletter-field{position:absolute;left:581px;top:2428px;width:416px;height:36px;border-bottom:1px solid #9a9a9a}
.newsletter-field span{position:absolute;left:14px;top:11px;font-size:13px;color:#8a8a8a}

/* footer */
.site-footer{position:absolute;left:0;top:2521px;width:1200px;height:354px;background:linear-gradient(150deg,#2e3033 0%,#1e2022 60%,#2b2c2e 100%);color:var(--white)}
.footer-brand{position:absolute;left:77px;top:40px;display:flex;align-items:center;gap:12px}
.footer-brand .brand-mark{width:26px;height:26px;background:var(--white)}
.footer-brand .brand-name{font-size:22px;color:var(--white)}
.footer-about{position:absolute;left:77px;top:118px;width:230px;font-size:14.5px;line-height:26px}
.footer-col h4{position:absolute;top:50px;font-family:"Alegreya Sans",sans-serif;font-weight:400;font-size:20px;letter-spacing:.5px}
.sitemap{position:absolute;left:349px;top:96px;list-style:none}
.sitemap li{font-size:15px;height:42px;padding-left:22px;position:relative}
.sitemap li::before{content:"";position:absolute;left:0;top:7px;width:6px;height:6px;background:var(--white)}
.news-item{position:absolute;left:619px;display:flex;gap:22px}
.news-thumb{width:62px;height:62px;background:linear-gradient(160deg,#cfd6dc,#8e9aa6)}
.news-text{font-size:14.5px;line-height:25px}
.news-date{font-size:13px;font-style:italic}
.touch{position:absolute;left:889px;font-size:14.5px;line-height:25px;display:flex;gap:20px}
.touch svg{flex:none;margin-top:4px}
.social-foot{position:absolute;left:948px;top:240px;display:flex;gap:12px}
.social-foot span{width:28px;height:28px;border:1px solid var(--white);background:transparent}
.social-foot span:first-child{background:var(--white)}
.footer-rule{position:absolute;left:77px;top:296px;width:1046px;height:1px;background:#6d6e70}
.copyright{position:absolute;left:0;width:1200px;top:314px;text-align:center;font-size:14.5px}
</style>
</head>
<body>

<header class="site-header">
  <div class="brand"><span class="brand-mark"></span><span class="brand-name">BRIMFIELD CUTWORKS</span></div>
  <div class="contact-item" style="left:508px">
    <div class="contact-icon"><svg width="18" height="18" viewBox="0 0 24 24"><path fill="#fff" d="M6.6 10.8c1.4 2.8 3.8 5.1 6.6 6.6l2.2-2.2c.3-.3.7-.4 1-.2 1.1.4 2.3.6 3.6.6.6 0 1 .4 1 1V20c0 .6-.4 1-1 1C10.6 21 3 13.4 3 4c0-.6.4-1 1-1h3.5c.6 0 1 .4 1 1 0 1.3.2 2.5.6 3.6.1.3 0 .7-.2 1z"/></svg></div>
    <div><div class="contact-label">Call Us</div><div class="contact-value">01632 960418</div></div>
  </div>
  <div class="contact-item" style="left:700px">
    <div class="contact-icon"><svg width="18" height="14" viewBox="0 0 18 14"><rect x="1" y="1" width="16" height="12" fill="none" stroke="#fff" stroke-width="1.6"/><path d="M1 1l8 7 8-7" fill="none" stroke="#fff" stroke-width="1.6"/></svg></div>
    <div><div class="contact-label">E-mail</div><div class="contact-value">info@brimfieldcutworks.com</div></div>
  </div>
  <div class="social-top"><span></span><span></span><span></span></div>
</header>

<section class="hero">
  <svg class="hero-art" width="1200" height="583" viewBox="0 0 1200 583">
    <defs>
      <linearGradient id="heroPhoto" x1="0" y1="0" x2="1" y2="1">
        <stop offset="0" stop-color="#4a4440"/>
        <stop offset="0.45" stop-color="#8a8580"/>
        <stop offset="1" stop-color="#b8b2aa"/>
      </linearGradient>
    </defs>
    <polygon points="650,0 745,293 660,583 682,583 767,293 672,0" fill="var(--blue)"/>
    <polygon role="img" aria-label="Photo of a waterjet cutting head throwing sparks over a workpiece" points="0,0 645,0 740,293 655,583 0,583" fill="url(#heroPhoto)"/>
  </svg>
  <div class="hero-title"><div class="l1">BRIMFIELD</div><div class="l2">CUTWORKS</div></div>
  <p class="hero-text">Lorem Ipsum is simply dummy text of the printing and typesetting industry. Lorem Ipsum been the industry's standard dummy text</p>
  <div class="btn" style="left:987px;top:389px;width:134px;height:50px;font-size:17px">CONTACT US</div>
  <svg class="hero-arrows" width="116" height="40" viewBox="0 0 116 40">
    <polygon points="0,0 60,0 72,40 0,40" fill="var(--blue)"/>
    <polygon points="66,0 116,0 116,40 78,40" fill="var(--blue)"/>
    <path d="M42 20H22M28 14l-6 6 6 6" stroke="#fff" stroke-width="2" fill="none"/>
    <path d="M86 20h18M98 14l6 6-6 6" stroke="#fff" stroke-width="2" fill="none"/>
  </svg>
</section>

<nav class="main-nav">
  <svg class="nav-band" width="1044" height="61" viewBox="0 0 1044 61"><polygon points="0,0 1044,0 987,61 57,61" fill="var(--blue)"/></svg>
  <ul>
    <li style="left:307px">Home</li>
    <li style="left:418px">About Us</li>
    <li style="left:551px">Materials</li>
    <li style="left:683px">Gallery</li>
  </ul>
</nav>

<section class="welcome">
  <h2 class="abs heading welcome-kicker">Welcome To</h2>
  <h1 class="abs heading welcome-title">BRIMFIELD CUTWORKS</h1>
  <p class="abs heading lead" style="left:80px;top:858px;width:420px">Waterjet cutting offers a soloution where other technologies struggle</p>
  <p class="abs body-text" style="left:80px;top:935px;width:510px">Brimfield Cutworks is part of the Corvane Group who have been providing a model making and profile cutting service primarily to the film industry for over 10 years. We are used to working within tight timeframes with a fast turnaround for all aspects of Water Jet Profiling, Tile Water Jet Cutting, Abrasive Steel Cutting and Foam Water Jet Cutting.</p>
  <div class="btn" style="left:79px;top:1095px;width:134px;height:50px">LEARN MORE</div>
  <div class="frame" style="left:723px;top:738px;width:398px;height:408px"></div>
  <div class="photo" role="img" aria-label="Photo of a waterjet machine cutting a wet metal plate" style="left:619px;top:782px;width:428px;height:322px;background:linear-gradient(150deg,#1e3a4e,#6d9ab3 50%,#2a4c63)"></div>
</section>

<section class="gallery">
  <h2 class="gallery-title heading">Our GALLERY</h2>
  <div class="tile" role="img" aria-label="Gallery photo: waterjet head over a perforated plate" style="left:77px;top:136px;width:552px;height:209px;background:linear-gradient(135deg,#3f78b8,#6ea0d4 50%,#3e6fa6)">
    <svg width="46" height="46" viewBox="0 0 46 46" style="position:absolute;left:252px;top:82px"><circle cx="18" cy="18" r="14" fill="none" stroke="#fff" stroke-width="3"/><path d="M28 28l14 14M18 11v14M11 18h14" stroke="#fff" stroke-width="3"/></svg>
  </div>
  <div class="tile" role="img" aria-label="Gallery photo: cutting head spraying water" style="left:638px;top:136px;width:213px;height:209px;background:linear-gradient(160deg,#6a5a5a,#c7a6a8)"></div>
  <div class="tile" role="img" aria-label="Gallery photo: machine cutting white sheet" style="left:861px;top:136px;width:262px;height:209px;background:linear-gradient(160deg,#5e7ea8,#d8e2ee)"></div>
  <div class="tile" role="img" aria-label="Gallery photo: cut green glass angle" style="left:77px;top:352px;width:212px;height:209px;background:linear-gradient(160deg,#5b8a80,#aee0b0)"></div>
  <div class="tile" role="img" aria-label="Gallery photo: cutting head over metal parts" style="left:293px;top:352px;width:226px;height:209px;background:linear-gradient(160deg,#4e4f52,#b8b9bc)"></div>
  <div class="tile" role="img" aria-label="Gallery photo: nozzle over green cut shapes" style="left:527px;top:352px;width:324px;height:209px;background:linear-gradient(160deg,#2a2e30,#4b8070 60%,#8ec3b0)"></div>
  <div class="tile" role="img" aria-label="Gallery photo: blue lit cutting bed" style="left:857px;top:352px;width:266px;height:209px;background:linear-gradient(160deg,#2a3c8c,#4e6fd0 55%,#1a2350)"></div>
</section>

<section class="materials">
  <div class="frame" style="left:77px;top:1896px;width:396px;height:406px"></div>
  <div class="photo" role="img" aria-label="Photo of a waterjet nozzle cutting under blue water" style="left:151px;top:1938px;width:426px;height:322px;background:linear-gradient(150deg,#3d6fa8,#8fc0e6 50%,#2f5c8f)"></div>
  <h2 class="abs heading" style="left:623px;top:1893px;font-size:38px;color:var(--blue)">MATERIALS</h2>
  <p class="abs heading lead" style="left:623px;top:1963px;width:460px">It is possible to cut virtually any profile in any material with waterjet</p>
  <p class="abs body-text" style="left:623px;top:2035px;width:420px">Materials we can cut include, but are not limited to, all metals and alloys, stone and ceramics, composites, solid surface, wood, glass, acrylics, resins, silicones, plastics, foams, carpet and felts. We can also cut laminated dissimilar materials which can often be very hard to cut using conventional methods. We are always happy to testof charge to demonstrate the quality of cut achievable.</p>
  <div class="btn" style="left:621px;top:2250px;width:134px;height:50px">LEARN MORE</div>
</section>

<section class="newsletter">
  <div class="newsletter-band"></div>
  <h3 class="heading">Newsletter For Receive</h3>
  <p class="heading">Our Latest Company Update</p>
  <svg width="40" height="40" viewBox="0 0 40 40" style="position:absolute;left:500px;top:58px"><polygon points="20,0 40,20 20,40 0,20" fill="#fff"/><rect x="13" y="15" width="14" height="10" fill="none" stroke="var(--blue)" stroke-width="1.5"/><path d="M13 15l7 6 7-6" fill="none" stroke="var(--blue)" stroke-width="1.5"/></svg>
</section>
<div class="newsletter-field"><span>Your E-mail Address*</span>
  <svg width="20" height="18" viewBox="0 0 20 18" style="position:absolute;right:12px;top:8px"><polygon points="0,8 20,0 14,18 10,11" fill="var(--blue)"/></svg>
</div>

<footer class="site-footer">
  <div class="footer-brand"><span class="brand-mark"></span><span class="brand-name">BRIMFIELD</span></div>
  <p class="footer-about">Lorem Ipsum is simply dummy text of the printing and typesetting industry. Lorem Ipsum has been unknown printer took a and scrambled it to make a type specimen book.</p>
  <div class="footer-col"><h4 style="left:349px">SITE MAP</h4></div>
  <ul class="sitemap"><li>Home</li><li>About us</li><li>Materials</li><li>Gallery</li></ul>
  <div class="footer-col"><h4 style="left:619px">LATEST NEWS</h4></div>
  <div class="news-item" style="top:94px"><div class="news-thumb" role="img" aria-label="News author portrait"></div><div class="news-text">Lorem Ipsum is and<br>typesetting industry.<div class="news-date">11 April 2018</div></div></div>
  <div class="news-item" style="top:186px"><div class="news-thumb" role="img" aria-label="News author portrait"></div><div class="news-text">Lorem Ipsum is and<br>typesetting industry.<div class="news-date">11 April 2018</div></div></div>
  <div class="footer-col"><h4 style="left:889px">GET IN TOUCH</h4></div>
  <div class="touch" style="top:94px"><svg width="16" height="20" viewBox="0 0 16 20"><path d="M8 0a7 7 0 0 0-7 7c0 5 7 13 7 13s7-8 7-13a7 7 0 0 0-7-7zm0 10a3 3 0 1 1 0-6 3 3 0 0 1 0 6z" fill="#fff"/></svg><div>123, Lorem Ipsum is and<br>typesetting industry.</div></div>
  <div class="touch" style="top:158px"><svg width="16" height="16" viewBox="0 0 24 24"><path fill="#fff" d="M6.6 10.8c1.4 2.8 3.8 5.1 6.6 6.6l2.2-2.2c.3-.3.7-.4 1-.2 1.1.4 2.3.6 3.6.6.6 0 1 .4 1 1V20c0 .6-.4 1-1 1C10.6 21 3 13.4 3 4c0-.6.4-1 1-1h3.5c.6 0 1 .4 1 1 0 1.3.2 2.5.6 3.6.1.3 0 .7-.2 1z"/></svg><div>01632 960418</div></div>
  <div class="touch" style="top:200px"><svg width="18" height="14" viewBox="0 0 18 14"><rect x="0" y="0" width="18" height="14" fill="#fff"/><path d="M0 0l9 8 9-8" fill="none" stroke="#26282b" stroke-width="1.5"/></svg><div>info@brimfieldcutworks.com</div></div>
  <div class="social-foot"><span></span><span></span><span></span></div>
  <div class="footer-rule"></div>
  <p class="copyright">© BRIMFIELD CUTWORKS - 2018. All Rights Reserved.</p>
</footer>

</body>
</html>
```